New Web Site - Professional Cleaning Company

I want to create a new attractive website that acts as an advertisement to visitors to entice them to reach out for more information.
We are a commercial/business janitorial service - with a new logo, would like the font to be complimentary to the font of logo, as well as the color scheme.
Target Market(s)
Commercial buildings, schools & medical buildings
Industry/Entity Type
Janitorial
Coding
Coded - Design and coding required
Number of Pages Required
4 page
Requirements
Must have
- Professionalism, sharp imagery

```html
<!DOCTYPE html>
<html lang="en">
<head>
<meta charset="utf-8">
<title>Brightway Facility Services</title>
<link href="https://fonts.googleapis.com/css2?family=Barlow+Condensed:wght@500;600;700&family=Barlow:wght@500;600;700&family=Open+Sans:wght@400;600&display=swap" rel="stylesheet">
<style>
:root{
  --navy:#1c3c78;
  --blue:#2590d6;
  --green:#3aaa35;
  --green-dark:#2c8f2a;
  --ink:#33404f;
  --muted:#6b7785;
  --pale:#eef6fb;
  --line:#dde6ee;
  --white:#ffffff;
}
*{box-sizing:border-box;margin:0;padding:0}
html,body{width:1200px;height:4312px;overflow:hidden;background:var(--white)}
body{font-family:"Open Sans",sans-serif;color:var(--ink);font-size:13px;line-height:1.6}
h1,h2,h3,.heading{font-family:"Barlow Condensed",sans-serif;text-transform:uppercase;letter-spacing:.5px}
.eyebrow{font-family:"Barlow",sans-serif;font-weight:600;font-size:12px;letter-spacing:1.5px;color:var(--green);text-transform:uppercase}
.btn{display:inline-block;font-family:"Barlow",sans-serif;font-weight:600;font-size:12px;letter-spacing:1px;text-transform:uppercase;color:var(--white);background:var(--green);border-radius:20px;padding:9px 24px}
.btn.blue{background:var(--blue)}
.photo{display:block}

/* header */
.site-header{height:110px;display:flex;align-items:center;justify-content:space-between;padding:0 60px;background:var(--white);box-shadow:0 2px 8px rgba(0,0,0,.06);position:relative;z-index:2}
.brand{display:flex;align-items:center;gap:12px}
.brand-dot{width:46px;height:46px;border-radius:50%;background:var(--blue)}
.brand-name{font-family:"Barlow",sans-serif;font-weight:700;font-size:18px;color:var(--navy);line-height:1.1;width:130px}
.nav{display:flex;gap:34px;font-family:"Barlow",sans-serif;font-weight:600;font-size:14px;color:var(--navy)}
.header-tools{display:flex;align-items:center;gap:16px;font-family:"Barlow",sans-serif;font-weight:600;color:var(--navy);font-size:14px}
.phone{display:flex;align-items:center;gap:6px}
.search{width:34px;height:34px;border-radius:50%;border:2px solid var(--navy);display:flex;align-items:center;justify-content:center}

/* hero */
.hero{height:600px;position:relative;overflow:hidden}
.hero .photo{position:absolute;inset:0;background:linear-gradient(120deg,#3b434d,#6d7682 45%,#2e353e)}
.hero-copy{position:absolute;left:120px;top:110px;width:560px;color:var(--white)}
.hero-copy .kicker{font-family:"Barlow",sans-serif;font-weight:600;letter-spacing:2px;font-size:15px;margin-bottom:10px}
.hero-copy h1{font-size:52px;line-height:1.05;font-weight:700;margin-bottom:26px}
.hero-wave{position:absolute;left:0;bottom:0}

/* about */
.about{height:500px;display:flex;gap:60px;padding:50px 120px 0;background:var(--white)}
.about .photo{width:380px;height:400px;background:linear-gradient(160deg,#dfe8ee,#b8c9d4 60%,#86a6b8);border-bottom:6px solid var(--green)}
.about-copy{flex:1;padding-top:20px}
.about-copy h2{font-size:36px;line-height:1.1;color:var(--navy);margin:8px 0 18px}
.about-copy p{margin-bottom:14px;color:var(--muted)}

/* services */
.services{height:460px;background:var(--pale);text-align:center;padding-top:50px}
.services h2{font-size:38px;color:var(--navy);margin-bottom:34px}
.service-grid{display:flex;gap:18px;justify-content:center}
.service-card{width:190px;background:var(--white);box-shadow:0 2px 8px rgba(0,0,0,.08)}
.service-card .photo{height:200px}
.service-card span{display:block;padding:12px 0;font-family:"Barlow",sans-serif;font-weight:600;font-size:12px;letter-spacing:1px;color:var(--navy);text-transform:uppercase}

/* sectors */
.sectors-head{height:120px;background:linear-gradient(var(--pale) 50%,var(--white) 50%);display:flex;justify-content:center;align-items:center}
.sectors-head h2{background:var(--navy);color:var(--white);font-size:28px;padding:12px 70px;border-radius:30px 30px 0 0}
.sector{position:relative;display:flex;overflow:hidden;border-bottom:1px solid var(--line)}
.sector .copy{width:560px;padding:36px 60px 0 120px;background:var(--white);position:relative;z-index:1}
.sector.flip{flex-direction:row-reverse}
.sector.flip .copy{padding:36px 120px 0 60px;width:640px}
.sector .photo{flex:1}
.sector h3{font-size:36px;color:var(--navy);font-weight:600;margin-bottom:10px}
.sector p{color:var(--muted);margin-bottom:10px;font-size:12.5px}
.sector ul{list-style:none;margin-bottom:16px}
.sector li{font-size:12px;color:var(--ink);padding-left:14px;position:relative;font-weight:600}
.sector li:before{content:"";position:absolute;left:0;top:7px;width:6px;height:6px;border-radius:50%;background:var(--green)}
.cta-bar{height:50px;background:var(--green);color:var(--white);display:flex;align-items:center;justify-content:center;font-family:"Barlow",sans-serif;font-weight:600;letter-spacing:1.5px;font-size:14px}

/* testimonials */
.testimonials{height:400px;text-align:center;padding-top:46px;position:relative}
.testimonials h2{font-size:38px;color:var(--navy);margin:4px 0 20px}
.avatar{width:70px;height:70px;border-radius:50%;background:#c9d6df;margin:0 auto 16px;border:3px solid var(--white);box-shadow:0 0 0 2px var(--green)}
.testimonials blockquote{width:640px;margin:0 auto 10px;color:var(--muted);font-size:12.5px}
.reviewer{font-family:"Barlow",sans-serif;font-weight:600;color:var(--navy);font-size:13px}
.stars{color:#f2b01e;letter-spacing:3px;margin-bottom:14px}
.arrow{position:absolute;top:190px;width:36px;height:36px;border-radius:50%;border:1px solid var(--line);display:flex;align-items:center;justify-content:center}

/* quote */
.quote{height:560px;position:relative;overflow:hidden;background:linear-gradient(#f6fafc,#e3eef5)}
.quote .backdrop{position:absolute;left:0;top:0;width:620px;height:100%;background:linear-gradient(120deg,#d9e4ea,#b7c8d2)}
.quote .cleaner{position:absolute;right:60px;top:40px;width:520px;height:520px;background:linear-gradient(170deg,#e8eef2,#a9bfca 55%,#3f8d45)}
.quote-form{position:absolute;left:160px;top:150px;width:380px;background:var(--navy);padding:28px 30px 32px;color:var(--white)}
.quote-form h2{font-size:30px;margin-bottom:2px}
.quote-form .sub{font-size:12px;opacity:.8;margin-bottom:16px}
.field-row{display:flex;gap:10px;margin-bottom:10px}
.field{flex:1;height:34px;background:var(--white);color:#9aa4ae;font-size:12px;padding:8px 10px}
.field.area{height:80px}
.quote-form .btn{margin-top:6px;display:block;width:90px;margin-left:auto;margin-right:auto;text-align:center;padding:8px 0}

/* footer */
.site-footer{height:272px;background:var(--pale);position:relative;padding:46px 120px 0;display:flex;gap:70px}
.site-footer .brand-dot{width:64px;height:64px}
.site-footer h4{font-family:"Barlow",sans-serif;font-weight:700;color:var(--navy);font-size:15px;margin-bottom:10px;text-transform:uppercase}
.footer-col{font-size:12px;color:var(--muted);line-height:1.9}
.socials{display:flex;gap:8px}
.socials span{width:26px;height:26px;border-radius:50%;background:var(--green)}
.copyright{position:absolute;left:0;right:0;bottom:0;height:46px;border-top:1px solid var(--line);display:flex;align-items:center;padding:0 120px;font-size:11px;color:var(--muted)}
</style>
</head>
<body>

<header class="site-header">
  <div class="brand"><span class="brand-dot"></span><span class="brand-name">Brightway Facility Services</span></div>
  <nav class="nav"><span>About Us</span><span>Services</span><span>Industry</span><span>Review</span><span>Contact</span></nav>
  <div class="header-tools">
    <span class="phone"><svg width="14" height="14" viewBox="0 0 24 24"><path fill="#3aaa35" d="M6.6 10.8a15 15 0 006.6 6.6l2.2-2.2c.3-.3.7-.4 1-.2 1.1.4 2.3.6 3.6.6.6 0 1 .4 1 1V20c0 .6-.4 1-1 1A17 17 0 013 4c0-.6.4-1 1-1h3.5c.6 0 1 .4 1 1 0 1.3.2 2.5.6 3.6.1.3 0 .7-.2 1z"/></svg>(555) 014-2288</span>
    <span class="search"><svg width="14" height="14" viewBox="0 0 24 24"><circle cx="10" cy="10" r="6" fill="none" stroke="#1c3c78" stroke-width="3"/><path d="M15 15l6 6" stroke="#1c3c78" stroke-width="3"/></svg></span>
    <span class="btn blue">Contact Us / Quote</span>
  </div>
</header>

<section class="hero">
  <div class="photo" role="img" aria-label="Grayscale photo of a cleaning crew working in a modern open-plan office"></div>
  <div class="hero-copy">
    <div class="kicker">COMMERCIAL JANITORIAL SERVICES</div>
    <h1>Cleaning that delivers a higher level of excellence and safety</h1>
    <span class="btn">Get a Quote</span>
  </div>
  <svg class="hero-wave" width="1200" height="260" viewBox="0 0 1200 260">
    <path d="M0 90 C220 250 520 260 760 170 C950 100 1080 90 1200 110 L1200 260 L0 260Z" fill="#eef6fb"/>
    <path d="M0 60 C200 230 520 240 760 150 C950 80 1080 70 1200 90" fill="none" stroke="#3aaa35" stroke-width="18"/>
    <path d="M0 120 C240 270 540 270 780 190 C960 130 1090 120 1200 135 L1200 260 L0 260Z" fill="#ffffff"/>
  </svg>
</section>

<section class="about">
  <div class="photo" role="img" aria-label="Photo of a cleaner in a green apron wiping a glass surface"></div>
  <div class="about-copy">
    <div class="eyebrow">Who We Are</div>
    <h2>Lorem ipsum is simply dummy text the printing typesetting.</h2>
    <p>We keep offices, schools and medical buildings spotless with trained crews, proven checklists and eco-friendly products. Every visit is planned around your schedule so work never stops.</p>
    <p>Our supervisors inspect each site, track results and report back, giving you clear proof of a cleaner and safer building.</p>
    <p>Family owned and locally run, we treat every facility as if it were our own and build partnerships that last for years.</p>
    <span class="btn blue">About Us</span>
  </div>
</section>

<section class="services">
  <div class="eyebrow">What We Do</div>
  <h2>Services We Offer</h2>
  <div class="service-grid">
    <div class="service-card"><div class="photo" role="img" aria-label="Photo of a freshly cleaned office corridor" style="background:linear-gradient(#8a7a66,#c9b79b)"></div><span>Carpet Cleaning</span></div>
    <div class="service-card"><div class="photo" role="img" aria-label="Photo of a polished lobby floor" style="background:linear-gradient(#6e5a44,#d8c7aa)"></div><span>Floor Care</span></div>
    <div class="service-card"><div class="photo" role="img" aria-label="Photo of a cleaner wiping a kitchen counter" style="background:linear-gradient(#b9c7cf,#7f9aa8)"></div><span>Commercial Kitchen Cleaning</span></div>
    <div class="service-card"><div class="photo" role="img" aria-label="Photo of a worker washing office windows" style="background:linear-gradient(#7fb0dd,#d5e6f3)"></div><span>Window Cleaning</span></div>
    <div class="service-card"><div class="photo" role="img" aria-label="Photo of a technician disinfecting a room" style="background:linear-gradient(#596a7d,#a3b4c4)"></div><span>Disinfecting</span></div>
  </div>
</section>

<div class="sectors-head"><h2>Solutions by Sector</h2></div>

<section class="sector" style="height:300px">
  <div class="copy">
    <h3>Industrial</h3>
    <p>Plants and warehouses need safe, hazard-free floors. Our crews handle heavy soil, dust and spills with industrial equipment and strict safety steps.</p>
    <ul><li>Factories</li><li>Warehouses</li><li>Distribution centers</li></ul>
    <span class="btn">Read More</span>
  </div>
  <div class="photo" role="img" aria-label="Photo of a worker operating a floor scrubber in a warehouse" style="background:linear-gradient(90deg,#ffffff,#c8d3da 30%,#7e8d96)"></div>
</section>

<section class="sector flip" style="height:320px">
  <div class="copy">
    <h3>Commercial &amp; Facility</h3>
    <p>Office towers and shared facilities stay fresh with nightly service, restroom care and lobby upkeep that impresses tenants and guests.</p>
    <ul><li>Multi-tenant office buildings</li><li>Single-tenant offices</li><li>Shared lobbies and common areas</li></ul>
    <span class="btn">Read More</span>
  </div>
  <div class="photo" role="img" aria-label="Photo of glass office towers against a bright sky" style="background:linear-gradient(90deg,#4f7fa8,#a9c8e0 70%,#ffffff)"></div>
</section>

<section class="sector" style="height:300px">
  <div class="copy">
    <h3>Healthcare</h3>
    <p>Clinics and medical offices rely on us for infection control, trained staff and careful cleaning of patient and exam areas.</p>
    <ul><li>Medical office buildings</li><li>Surgery centers</li><li>Dental and vision clinics</li></ul>
    <span class="btn">Read More</span>
  </div>
  <div class="photo" role="img" aria-label="Photo of a bright clinic reception desk" style="background:linear-gradient(90deg,#ffffff,#e6eef2 30%,#b9ccd6)"></div>
</section>

<section class="sector flip" style="height:320px">
  <div class="copy">
    <h3>Government</h3>
    <p>Public buildings and schools need reliable, secure service. Our vetted teams follow every access rule and keep spaces ready for the public.</p>
    <ul><li>Municipal buildings and courts</li><li>Schools and campuses</li><li>Libraries and community centers</li></ul>
    <span class="btn">Read More</span>
  </div>
  <div class="photo" role="img" aria-label="Photo of a columned government building under a blue sky" style="background:linear-gradient(90deg,#6f8fb0,#c9d3d8 60%,#ffffff)"></div>
</section>

<div class="cta-bar">CONTACT US FOR A FREE QUOTE TODAY</div>

<section class="testimonials">
  <div class="eyebrow">Testimonials</div>
  <h2>Happy Clients Say</h2>
  <div class="avatar" role="img" aria-label="Client portrait"></div>
  <blockquote>Their team has kept our building spotless for three years. They are on time, easy to reach and always go the extra step. Our staff and visitors notice the difference every single day, and we would gladly recommend them.</blockquote>
  <div class="reviewer">Dana Reyes, Office Manager</div>
  <div class="stars">★★★★★</div>
  <span class="btn blue">View All</span>
  <span class="arrow" style="left:150px"><svg width="10" height="14" viewBox="0 0 10 14"><path d="M8 1L2 7l6 6" fill="none" stroke="#1c3c78" stroke-width="2"/></svg></span>
  <span class="arrow" style="right:150px"><svg width="10" height="14" viewBox="0 0 10 14"><path d="M2 1l6 6-6 6" fill="none" stroke="#1c3c78" stroke-width="2"/></svg></span>
</section>

<section class="quote">
  <div class="backdrop" role="img" aria-label="Faded photo of a cleaner mopping an office floor"></div>
  <div class="cleaner" role="img" aria-label="Photo of a smiling cleaner in a green apron and yellow gloves"></div>
  <svg style="position:absolute;right:0;top:30px" width="420" height="260" viewBox="0 0 420 260"><path d="M60 20 C200 0 360 60 420 200" fill="none" stroke="#3aaa35" stroke-width="16"/></svg>
  <div class="quote-form">
    <h2>Get Free Quote</h2>
    <div class="sub">Schedule your free service visit today</div>
    <div class="field-row"><div class="field">Name</div><div class="field">Email</div></div>
    <div class="field-row"><div class="field">Phone</div><div class="field">Company</div></div>
    <div class="field-row"><div class="field">Service</div></div>
    <div class="field-row"><div class="field area">Message</div></div>
    <span class="btn">Send</span>
  </div>
</section>

<footer class="site-footer">
  <div class="brand"><span class="brand-dot"></span><span class="brand-name">Brightway Facility Services</span></div>
  <div class="footer-col" style="width:260px">
    <h4>Contact Us</h4>
    <div>(555) 014-2288</div>
    <div>hello@brightwayfs.example</div>
    <div>418 Harbor Lane, Suite 12, Riverton, ST 00412</div>
  </div>
  <div class="footer-col">
    <h4>Quick Links</h4>
    <div>Home</div><div>About Us</div><div>Services</div><div>Industry</div><div>Contact</div>
  </div>
  <div class="footer-col">
    <h4>Follow Us</h4>
    <div class="socials"><span></span><span></span><span></span><span></span></div>
  </div>
  <div class="copyright">© 2024 Brightway Facility Services. All rights reserved.</div>
</footer>

</body>
</html>
```